Business Card Design

Business card design.

Business card is to have logo, website address and email address.

Website is www.brightkettle.ie
Email is info@brightkettle.ie

I have ordered Business Card Printing via Print Harbor, the Double-sided colour printed option with gloss finish.

Industry/Entity Type

Business

```html
<!DOCTYPE html>
<html lang="en">
<head>
<meta charset="utf-8">
<title>Bright Kettle Business Card</title>
<link rel="stylesheet" href="https://fonts.googleapis.com/css2?family=Nunito:wght@800&family=Roboto:wght@500&display=swap">
<style>
  :root {
    --backdrop: #e4e4e6;
    --card-light: #ffffff;
    --card-dark: #0c0c0c;
    --ink: #111111;
    --ink-light: #ffffff;
    --accent: #d01a1f;
  }
  * { margin: 0; padding: 0; box-sizing: border-box; }
  html, body { width: 1200px; height: 960px; overflow: hidden; }
  body {
    background: var(--backdrop);
    display: flex;
    flex-direction: column;
    align-items: center;
    justify-content: center;
    gap: 56px;
  }
  .card {
    width: 600px;
    height: 343px;
    display: flex;
    flex-direction: column;
    align-items: center;
    justify-content: center;
    box-shadow: 0 6px 18px rgba(0,0,0,0.18);
  }
  .card--front { background: var(--card-light); }
  .card--back { background: var(--card-dark); }
  .brand {
    display: flex;
    align-items: center;
    gap: 14px;
  }
  .brand__dot {
    width: 34px;
    height: 34px;
    border-radius: 50%;
    background: var(--accent);
    flex: none;
  }
  .brand__name {
    font-family: "Nunito", sans-serif;
    font-weight: 800;
    font-size: 46px;
    letter-spacing: 0.5px;
    color: var(--ink);
  }
  .card--back .brand__name { color: var(--ink-light); font-size: 50px; }
  .contact {
    margin-top: 48px;
    list-style: none;
    display: flex;
    flex-direction: column;
    gap: 8px;
  }
  .contact__item {
    display: flex;
    align-items: center;
    gap: 8px;
    font-family: "Roboto", sans-serif;
    font-weight: 500;
    font-size: 17px;
    color: var(--ink);
  }
  .contact__icon { width: 20px; height: 20px; flex: none; }
</style>
</head>
<body>
  <section class="card card--front" aria-label="Business card front">
    <div class="brand">
      <span class="brand__dot"></span>
      <span class="brand__name">BRIGHTKETTLE.IE</span>
    </div>
    <ul class="contact">
      <li class="contact__item">
        <svg class="contact__icon" viewBox="0 0 20 20" aria-hidden="true">
          <circle cx="10" cy="10" r="10" fill="#d01a1f"/>
          <rect x="5" y="6.5" width="10" height="7" fill="none" stroke="#111" stroke-width="1.3"/>
          <path d="M5 6.5 L10 10.8 L15 6.5" fill="none" stroke="#111" stroke-width="1.3"/>
        </svg>
        info@brightkettle.ie
      </li>
      <li class="contact__item">
        <svg class="contact__icon" viewBox="0 0 20 20" aria-hidden="true">
          <circle cx="10" cy="10" r="10" fill="#d01a1f"/>
          <circle cx="10" cy="10" r="5.5" fill="none" stroke="#111" stroke-width="1.2"/>
          <ellipse cx="10" cy="10" rx="2.4" ry="5.5" fill="none" stroke="#111" stroke-width="1.1"/>
          <path d="M4.5 10 H15.5 M5.3 7.3 H14.7 M5.3 12.7 H14.7" stroke="#111" stroke-width="1"/>
        </svg>
        www.brightkettle.ie
      </li>
    </ul>
  </section>

  <section class="card card--back" aria-label="Business card back">
    <div class="brand">
      <span class="brand__dot"></span>
      <span class="brand__name">BRIGHTKETTLE.IE</span>
    </div>
  </section>
</body>
</html>
```